RLG Biz Cards and Web Page Design

Hello we are a credit card processing company, a lending company, and payroll company. Seeing how this is a card. I would like to see some clever designs... You could make it look like a credit card, with raised lettering and signature spot on the back. Be creative.
Also this is for a webpage. Our website is www.ridgecrestledgergroup.com
Please let me know what you need.

Target Market(s)

Business Owners in the USA.

Industry/Entity Type

Credit Card

Contact Information for Business Card

I've attached our current logo and business cards. I would like you to use the Red, White, and Blue Colors and also maybe try designs that look like credit cards with Raised Text, signature spot in the back and mag strips.

Number of Pages Required

1 page

```html
<!DOCTYPE html>
<html lang="en">
<head>
<meta charset="utf-8">
<title>RLG Business Card</title>
<link href="https://fonts.googleapis.com/css2?family=Montserrat:wght@400;500;600;700&display=swap" rel="stylesheet">
<style>
  :root {
    --stage: #1d1d1f;
    --card-blue: #2d3cae;
    --card-blue-light: #4150c0;
    --emboss-face: #3a49b8;
    --emboss-light: rgba(255,255,255,0.38);
    --emboss-dark: rgba(8,14,70,0.55);
    --navy: #22318f;
    --red: #e01d2b;
    --ink: #3a3a3a;
    --white: #ffffff;
    --stripe: #1a1a1a;
    --silver: #e9eaee;
  }
  * { box-sizing: border-box; margin: 0; padding: 0; }
  html, body { width: 1200px; height: 929px; overflow: hidden; }
  body { background: var(--stage); font-family: "Montserrat", sans-serif; position: relative; }

  .card { position: absolute; width: 540px; height: 310px; border-radius: 18px; overflow: hidden; }

  /* Back */
  .card-back { left: 110px; top: 100px; background: linear-gradient(135deg, var(--card-blue-light), var(--card-blue)); }
  .mag-stripe { position: absolute; left: 0; right: 0; top: 26px; height: 28px; background: var(--stripe); }
  .signature-strip { position: absolute; left: 30px; top: 70px; width: 400px; height: 30px; background: linear-gradient(90deg, var(--silver), #f7f7f9 60%, var(--silver)); display: flex; justify-content: flex-end; }
  .signature-strip .cvv-box { width: 70px; height: 100%; border-left: 2px solid var(--card-blue); background: var(--white); }
  .embossed {
    color: var(--emboss-face);
    text-shadow: -1px -1px 0 var(--emboss-light), 1px 1px 1px var(--emboss-dark), 2px 2px 3px rgba(8,14,70,0.25);
  }
  .back-brand { position: absolute; left: 120px; top: 150px; display: flex; align-items: center; gap: 16px; }
  .back-brand .mark { font-size: 38px; font-weight: 600; letter-spacing: 1px; }
  .back-brand .divider { width: 1px; height: 60px; background: var(--emboss-dark); box-shadow: 1px 0 0 var(--emboss-light); }
  .back-brand .wordmark { font-size: 15px; font-weight: 600; letter-spacing: 1.5px; line-height: 1.3; }
  .embossed-number { position: absolute; left: 40px; bottom: 34px; font-size: 17px; letter-spacing: 3px; font-weight: 500; }

  /* Front */
  .card-front { left: 560px; top: 500px; background: var(--white); }
  .front-brand { position: absolute; left: 34px; top: 30px; display: flex; align-items: center; gap: 14px; }
  .front-brand .mark { display: flex; align-items: center; gap: 8px; font-size: 32px; font-weight: 700; color: var(--navy); }
  .front-brand .mark::before { content: ""; width: 14px; height: 14px; background: var(--red); }
  .front-brand .divider { width: 1.5px; height: 54px; background: var(--red); }
  .front-brand .wordmark { font-size: 13px; font-weight: 700; color: var(--navy); letter-spacing: 1.2px; line-height: 1.35; }
  .person { position: absolute; right: 30px; top: 90px; text-align: right; }
  .person .name { font-size: 18px; font-weight: 600; color: var(--navy); line-height: 1.2; }
  .person .title { font-size: 11px; font-weight: 600; color: var(--ink); letter-spacing: 0.5px; margin-top: 3px; }
  .rule { position: absolute; left: 34px; right: 30px; top: 142px; height: 1.5px; background: var(--navy); }
  .contacts { position: absolute; left: 34px; top: 158px; list-style: none; }
  .contacts li { display: flex; align-items: center; gap: 10px; font-size: 12px; color: var(--ink); line-height: 21px; }
  .contacts svg { width: 12px; height: 12px; fill: none; stroke: var(--red); stroke-width: 2; flex: none; }
  .address { position: absolute; right: 30px; top: 162px; text-align: right; font-size: 12px; color: var(--ink); line-height: 1.6; }
</style>
</head>
<body>
  <section class="card card-back" aria-label="Card back">
    <div class="mag-stripe"></div>
    <div class="signature-strip"><div class="cvv-box"></div></div>
    <div class="back-brand">
      <span class="mark embossed">RLG</span>
      <span class="divider"></span>
      <span class="wordmark embossed">RIDGECREST<br>LEDGER GROUP</span>
    </div>
    <div class="embossed-number embossed">123 P43 93W KJ0 PX2 1M78 0032 KG06</div>
  </section>

  <section class="card card-front" aria-label="Card front">
    <div class="front-brand">
      <span class="mark">RLG</span>
      <span class="divider"></span>
      <span class="wordmark">RIDGECREST<br>LEDGER GROUP</span>
    </div>
    <div class="person">
      <p class="name">DANIEL R. WHITCOMBE</p>
      <p class="title">DIRECTOR OF OPERATIONS</p>
    </div>
    <div class="rule"></div>
    <ul class="contacts">
      <li><svg viewBox="0 0 12 12"><path d="M2 1.5l2.5 0 1 2.5-1.5 1a6 6 0 0 0 3 3l1-1.5 2.5 1v2.5c-5 0-8.5-3.5-8.5-8.5z"/></svg>888-555-0142</li>
      <li><svg viewBox="0 0 12 12"><rect x="3" y="1" width="6" height="10" rx="1"/></svg>860-555-0178</li>
      <li><svg viewBox="0 0 12 12"><rect x="1.5" y="4.5" width="9" height="5"/><rect x="3.5" y="1.5" width="5" height="3"/></svg>877-555-0193</li>
      <li><svg viewBox="0 0 12 12"><rect x="1" y="2.5" width="10" height="7"/><path d="M1 2.5l5 4 5-4"/></svg>dwhitcombe@ridgecrestledger.com</li>
      <li><svg viewBox="0 0 12 12"><circle cx="5" cy="5" r="3.5"/><path d="M7.5 7.5l3 3"/></svg>www.ridgecrestledgergroup.com</li>
    </ul>
    <div class="address">18 Alder Lane<br>Madison, CT 06443</div>
  </section>
</body>
</html>
```